Redesign and move to Wordpress for quarvendo.com

Our website needs a redesign and at the same time we are moving it to Wordpress. Please help us with a new digital professional look and feel.

We are an Australian Software Engineering company specialising in advanced software development using in A.I., PLatform Engineering, Integration and Cloud. See the current quarvendo.com for more information about us.

```html
<!DOCTYPE html>
<html lang="en">
<head>
<meta charset="utf-8">
<title>quarvendo — Reliable Smart Software Engineering</title>
<link href="https://fonts.googleapis.com/css2?family=Orbitron:wght@400;500&family=Poppins:wght@300;400;500;600&display=swap" rel="stylesheet">
<style>
:root{
  --navy:#0b1538;
  --navy-deep:#070e2a;
  --blue:#125ca6;
  --blue-dark:#0f4f8f;
  --teal:#56c3b6;
  --pale:#f1f4fb;
  --ink:#1b1d2a;
  --muted:#555a66;
  --white:#ffffff;
  --line:#dde2ec;
}
*{margin:0;padding:0;box-sizing:border-box}
html,body{width:1200px;height:5172px;overflow:hidden}
body{font-family:"Poppins",sans-serif;color:var(--ink);background:var(--white)}
section,header,footer{position:relative;width:1200px;overflow:hidden}
.abs{position:absolute}
.heading{position:absolute;display:flex;align-items:center;gap:14px;font-family:"Orbitron",sans-serif;font-size:50px;color:var(--ink);letter-spacing:1px}
.heading .mark{width:34px;height:34px;border:3px solid var(--blue)}
.btn{position:absolute;display:flex;align-items:center;justify-content:center;gap:22px;font-weight:600;font-size:16px;letter-spacing:.3px}
.btn .arrow{width:26px;height:18px;border-radius:2px;display:flex;align-items:center;justify-content:center}
.btn-blue{background:var(--blue);color:var(--white)}
.btn-blue .arrow{background:var(--teal)}

/* header */
.site-header{height:125px;background:var(--navy-deep)}
.brand{left:66px;top:38px;display:flex;align-items:center;gap:14px;color:var(--white);font-size:34px;font-family:"Orbitron",sans-serif;letter-spacing:2px}
.brand .sq{width:42px;height:42px;border:3px solid var(--white)}
.nav a{position:absolute;top:52px;font-size:13px;color:var(--white);text-decoration:none;font-weight:500}
.nav .active{color:var(--teal);border-bottom:2px solid var(--teal);padding-bottom:10px}
.nav .nav-cta{top:40px;left:951px;width:135px;height:44px;border:2px solid var(--teal);display:flex;align-items:center;justify-content:center;background:transparent;color:var(--white)}

/* hero */
.hero{height:622px;background:radial-gradient(ellipse at 50% 45%,#1f3c9c 0%,#122571 40%,#0a1545 80%)}
.hero-title{left:0;width:1200px;top:150px;text-align:center;color:var(--white);font-family:"Orbitron",sans-serif;font-weight:400;font-size:58px;line-height:70px;letter-spacing:3px}
.hero .btn{left:496px;top:335px;width:210px;height:58px;background:var(--white);color:var(--blue)}
.hero .btn .arrow{background:var(--blue)}
.dots{left:563px;top:540px;display:flex;gap:6px}
.dots span{width:14px;height:14px;border-radius:50%;background:#8b90a6}
.dots span:first-child{background:var(--white)}

/* about */
.about{height:672px;background:var(--pale)}
.about .heading{left:134px;top:92px}
.about-text{left:134px;top:180px;width:502px;font-size:13.4px;line-height:27px;color:var(--muted);text-align:justify}
.about-text p+p{margin-top:27px}
.about .btn{left:134px;top:484px;width:213px;height:60px}
.photo{position:absolute}

/* services */
.services{height:994px;background:var(--white)}
.services .heading{left:352px;top:94px}
.svc-label{position:absolute;font-size:17px;font-weight:500;line-height:22px;color:var(--ink)}
.svc-label.right{text-align:right}

/* newsletter */
.newsletter{height:675px;background:linear-gradient(120deg,#2a3357 0%,#1b2445 45%,#2c3250 75%,#3b3f58 100%)}
.newsletter .mark{left:583px;top:104px;width:34px;height:34px;border:3px solid var(--white)}
.news-title{left:0;width:1200px;top:160px;text-align:center;color:var(--white);font-family:"Orbitron",sans-serif;font-weight:400;font-size:54px;line-height:69px;letter-spacing:2px}
.news-sub{left:0;width:1200px;top:386px;text-align:center;color:var(--white);font-size:34px;font-weight:300;letter-spacing:-.5px}
.subscribe{left:305px;top:490px;width:590px;height:60px;background:var(--teal);display:flex;align-items:center;justify-content:space-between;padding:0 18px 0 33px}
.subscribe .field{color:var(--white);font-size:14px;font-weight:500}
.subscribe .go{width:162px;height:42px;background:var(--blue);color:var(--white);font-size:14px;font-weight:500;display:flex;align-items:center;justify-content:center}

/* blog */
.blog{height:797px;background:var(--white)}
.blog .heading{left:430px;top:100px}
.post{position:absolute;top:227px;width:336px;height:380px}
.post .thumb{position:absolute;left:0;top:0;width:336px;height:229px}
.post .card{position:absolute;left:0;top:189px;width:285px;height:190px;background:var(--white);padding:18px 24px 0 24px}
.post .date{display:flex;align-items:center;gap:6px;font-size:12px;font-weight:500;color:var(--ink)}
.post .date i{width:11px;height:11px;border:2px solid var(--teal);display:block}
.post h3{margin-top:14px;font-size:16px;line-height:27px;font-weight:600;color:var(--blue)}
.post .more{position:absolute;left:24px;top:172px;font-size:12px;font-weight:600;color:var(--teal);text-decoration:underline}
.blog .btn{left:494px;top:657px;width:213px;height:60px}

/* contact */
.contact-section{height:697px;background:var(--pale)}
.contact-section .heading{left:600px;top:104px}
.input{position:absolute;background:var(--white);border:1px solid var(--line);font-size:14px;color:#8a8f9c;padding:16px 22px}
.contact-section .btn{left:600px;top:533px;width:213px;height:58px}

/* clients */
.clients{height:189px;background:var(--white)}
.client{position:absolute;top:64px;display:flex;align-items:center;gap:10px;font-size:32px;font-weight:600;color:#2f3136;letter-spacing:-.5px}
.client .sq{width:26px;height:26px;background:#2f3136}
.client .ci{width:24px;height:24px;border-radius:50%;background:#2f3136}

/* footer */
.site-footer{height:401px;background:var(--blue)}
.f-head{position:absolute;top:88px;font-family:"Orbitron",sans-serif;font-size:22px;color:var(--white);letter-spacing:1px}
.f-rule{left:100px;top:122px;width:1032px;height:1px;background:rgba(255,255,255,.35)}
.f-list{position:absolute;top:154px;list-style:none}
.f-list li{font-size:13px;line-height:26px;color:var(--white);display:flex;gap:10px}
.f-list li::before{content:"→";font-size:12px}
.f-contact{position:absolute;left:869px;display:flex;gap:14px;color:var(--white);font-size:12.5px;line-height:17px}
.f-contact .ic{width:26px;height:26px;border-radius:4px;background:var(--white);display:flex;align-items:center;justify-content:center;flex:none}
.f-bottom{left:0;top:330px;width:1200px;height:1px;background:rgba(255,255,255,.3)}
.copy{left:68px;top:356px;font-size:11px;color:var(--white)}
.social{top:352px;width:22px;height:22px;background:var(--white);opacity:.9}
</style>
</head>
<body>

<header class="site-header">
  <div class="abs brand"><span class="sq"></span>quarvendo</div>
  <nav class="nav">
    <a class="active" style="left:568px">HOME</a>
    <a style="left:656px">ABOUT US</a>
    <a style="left:771px">SERVICES</a>
    <a style="left:880px">BLOG</a>
    <a class="nav-cta">CONTACT US</a>
  </nav>
  <svg class="abs" style="left:1110px;top:50px" width="26" height="26" viewBox="0 0 26 26" aria-label="Search"><circle cx="11" cy="11" r="8" fill="none" stroke="#fff" stroke-width="2"/><line x1="17" y1="17" x2="24" y2="24" stroke="#fff" stroke-width="2"/></svg>
</header>

<section class="hero" role="img" aria-label="Glowing blue circuit board background">
  <h1 class="abs hero-title">Reliable Smart<br>Software Engineering</h1>
  <a class="btn">KNOW MORE <span class="arrow"><svg width="14" height="10" viewBox="0 0 14 10"><path d="M0 5h12M8 1l4 4-4 4" stroke="#fff" stroke-width="2" fill="none"/></svg></span></a>
  <div class="abs dots"><span></span><span></span><span></span><span></span></div>
</section>

<section class="about">
  <h2 class="heading"><span class="mark"></span>About Us</h2>
  <div class="abs about-text">
    <p>Since our inception in 2013, we have been on a mission to make complex custom enterprise integration accessible to any organization, regardless of industry, size, or location.</p>
    <p>Our journey began with a focus on Integration Architecture, quickly moving into delivering bespoke systems integration using Northvale technologies like LinkHub, CoreNet, DataVault Server, and ServiceWire. Our commitment to excellence quickly earned us recognition, and in 2014, we became a proud Northvale Gold Partner, achieving this accolade with the creation of our first 100% native Nimbara cloud solution.</p>
  </div>
  <a class="btn btn-blue">READ MORE <span class="arrow"><svg width="14" height="10" viewBox="0 0 14 10"><path d="M0 5h12M8 1l4 4-4 4" stroke="#fff" stroke-width="2" fill="none"/></svg></span></a>
  <div class="photo" style="left:722px;top:154px;width:155px;height:107px;background:linear-gradient(135deg,#3d5f8a,#28344f)" role="img" aria-label="Team member working at a laptop"></div>
  <div class="photo" style="left:903px;top:154px;width:155px;height:209px;background:linear-gradient(160deg,#5a4a44,#2e2a33)" role="img" aria-label="Developer reviewing code on screen"></div>
  <div class="photo" style="left:722px;top:289px;width:155px;height:209px;background:linear-gradient(160deg,#465a78,#33323d)" role="img" aria-label="Engineer in a modern office"></div>
  <div class="photo" style="left:903px;top:389px;width:155px;height:109px;background:linear-gradient(135deg,#c49a7a,#8d6a58)" role="img" aria-label="Hands typing on a laptop"></div>
</section>

<section class="services">
  <h2 class="heading"><span class="mark"></span>Our Services</h2>
  <svg class="abs" style="left:0;top:0" width="1200" height="994" viewBox="0 0 1200 994">
    <defs>
      <filter id="soft" x="-20%" y="-20%" width="140%" height="140%"><feDropShadow dx="0" dy="4" stdDeviation="8" flood-color="#9aa3b5" flood-opacity=".35"/></filter>
    </defs>
    <circle cx="596" cy="559" r="220" fill="#fff" filter="url(#soft)"/>
    <circle cx="596" cy="559" r="172" fill="var(--teal)"/>
    <rect x="546" y="509" width="100" height="100" fill="none" stroke="#fff" stroke-width="8"/>
    <g fill="var(--teal)">
      <circle cx="496" cy="360" r="7"/><circle cx="689" cy="360" r="7"/>
      <circle cx="393" cy="474" r="7"/><circle cx="797" cy="474" r="7"/>
      <circle cx="385" cy="625" r="7"/><circle cx="803" cy="629" r="7"/>
      <circle cx="494" cy="756" r="7"/><circle cx="695" cy="756" r="7"/>
    </g>
    <g fill="none" stroke="#fff" stroke-width="2.2" stroke-linecap="round" stroke-linejoin="round">
      <g transform="translate(472 278)"><circle r="54" fill="#fff" stroke="var(--teal)" stroke-width="1.5"/><circle r="44" fill="var(--blue)" stroke="none"/><path d="M-16 16h32M-12 16v-10M-4 16v-18M4 16v-12M12 16v-22M-14 -4l8-8 8 6 12-12"/></g>
      <g transform="translate(721 278)"><circle r="54" fill="#fff" stroke="var(--teal)" stroke-width="1.5"/><circle r="44" fill="var(--blue)" stroke="none"/><circle cx="-12" cy="-12" r="4"/><circle cx="0" cy="-12" r="4"/><circle cx="12" cy="-12" r="4"/><circle cx="-14" cy="2" r="5"/><circle cx="0" cy="2" r="5"/><circle cx="14" cy="2" r="5"/><circle cx="-8" cy="16" r="4"/><circle cx="8" cy="16" r="4"/><path d="M-9 2h4M5 2h4"/></g>
      <g transform="translate(311 452)"><circle r="54" fill="#fff" stroke="var(--teal)" stroke-width="1.5"/><circle r="44" fill="var(--blue)" stroke="none"/><circle r="9"/><path d="M0-22v6M0 16v6M-22 0h6M16 0h6M-16-16l4 4M12 12l4 4M16-16l-4 4M-12 12l-4 4"/></g>
      <g transform="translate(881 452)"><circle r="54" fill="#fff" stroke="var(--teal)" stroke-width="1.5"/><circle r="44" fill="var(--blue)" stroke="none"/><circle cx="-12" cy="-12" r="5"/><circle cx="14" cy="-10" r="5"/><circle cx="-12" cy="14" r="5"/><circle cx="14" cy="14" r="5"/><circle cx="2" cy="2" r="4"/><path d="M-8-8l7 7M10-7l-5 6M-8 10l7-6M10 10l-5-5"/></g>
      <g transform="translate(301 643)"><circle r="54" fill="#fff" stroke="var(--teal)" stroke-width="1.5"/><circle r="44" fill="var(--blue)" stroke="none"/><path d="M-8 20v-8c-8-4-10-12-8-20 3-10 16-14 24-8 6 4 7 10 6 15l4 6h-5v7h-8v8"/><circle cx="2" cy="-6" r="3"/><circle cx="-4" cy="4" r="2.5"/></g>
      <g transform="translate(889 643)"><circle r="54" fill="#fff" stroke="var(--teal)" stroke-width="1.5"/><circle r="44" fill="var(--blue)" stroke="none"/><path d="M-14 6h30a8 8 0 0 0 0-16 12 12 0 0 0-22-4 9 9 0 0 0-8 20z"/><path d="M0 6v12M-8 6v8M8 6v8"/><circle cx="0" cy="20" r="2"/></g>
      <g transform="translate(472 844)"><circle r="54" fill="#fff" stroke="var(--teal)" stroke-width="1.5"/><circle r="44" fill="var(--blue)" stroke="none"/><rect x="-12" y="-22" width="22" height="10" rx="2"/><rect x="-18" y="-4" width="22" height="10" rx="2"/><rect x="-12" y="14" width="22" height="10" rx="2"/><path d="M10 1l8 0M14-3l4 4-4 4M-1-12v8M-4 6v8"/></g>
      <g transform="translate(721 844)"><circle r="54" fill="#fff" stroke="var(--teal)" stroke-width="1.5"/><circle r="44" fill="var(--blue)" stroke="none"/><path d="M-18-14h24v18h-14l-8 6v-6h-2z"/><path d="M10-6h8v18h-2v6l-8-6h-12v-4"/></g>
    </g>
  </svg>
  <div class="svc-label right" style="right:797px;top:238px">CUSTOM INTEGRATION<br>FOR SMALL to<br>MEDIUM BUSINESS</div>
  <div class="svc-label" style="left:797px;top:246px">ENTERPRISE<br>Systems<br>Integration</div>
  <div class="svc-label right" style="right:961px;top:420px">REal-time<br>DATA stream<br>PROCESSING</div>
  <div class="svc-label" style="left:953px;top:441px">Microservices</div>
  <div class="svc-label right" style="right:973px;top:620px">Pilot /<br>AI Agents</div>
  <div class="svc-label" style="left:963px;top:620px">PLATFORM<br>Engineering</div>
  <div class="svc-label right" style="right:805px;top:833px">IPAAS</div>
  <div class="svc-label" style="left:797px;top:833px">Conversational AI</div>
</section>

<section class="newsletter" role="img" aria-label="Blurred office desk with digital technology overlay">
  <div class="abs mark"></div>
  <h2 class="abs news-title">Australia's Largest<br>health charity implements<br>QUARVENDO API MSG BUS</h2>
  <p class="abs news-sub">Register to our newsletter to find out more.</p>
  <form class="abs subscribe"><span class="field">Enter Your Email Address</span><span class="go">Subscribe</span></form>
</section>

<section class="blog">
  <h2 class="heading"><span class="mark"></span>Our Blog</h2>
  <article class="post" style="left:68px">
    <div class="thumb" role="img" aria-label="Rows of server racks with green lights" style="background:linear-gradient(90deg,#0e2b14,#2f6a2a 30%,#0d2410 50%,#3f7f31 75%,#12301a)"></div>
    <div class="card"><div class="date"><i></i>June 24, 2024</div><h3>Why most upgrade paths for LinkHub lead to using Nimbara flow apps</h3><a class="more">READ MORE</a></div>
  </article>
  <article class="post" style="left:434px">
    <div class="thumb" role="img" aria-label="Desk with monitor showing data visuals" style="background:linear-gradient(120deg,#1b2a3a,#2b3440 45%,#7a6a4a 80%,#b8a27a)"></div>
    <div class="card"><div class="date"><i></i>June 14, 2024</div><h3>How to get visibility into your LinkHub environment</h3><a class="more">READ MORE</a></div>
  </article>
  <article class="post" style="left:797px">
    <div class="thumb" role="img" aria-label="Monitor showing a security vulnerability report" style="background:linear-gradient(160deg,#4a4d55,#d8dadf 45%,#e8e9ec 70%,#9ea1a8)"></div>
    <div class="card"><div class="date"><i></i>June 12, 2024</div><h3>Top 10 LinkHub Server Vulnerabilities and Security Recommendations</h3><a class="more">READ MORE</a></div>
  </article>
  <a class="btn btn-blue">VIEW MORE <span class="arrow"><svg width="14" height="10" viewBox="0 0 14 10"><path d="M0 5h12M8 1l4 4-4 4" stroke="#fff" stroke-width="2" fill="none"/></svg></span></a>
</section>

<section class="contact-section">
  <div class="photo" style="left:66px;top:123px;width:205px;height:162px;background:linear-gradient(135deg,#1d2f52,#3a5a86)" role="img" aria-label="Holographic technology interface"></div>
  <div class="photo" style="left:66px;top:285px;width:205px;height:290px;background:linear-gradient(160deg,#2d4a7a,#1a2540)" role="img" aria-label="Person interacting with digital icons"></div>
  <div class="photo" style="left:305px;top:123px;width:207px;height:285px;background:linear-gradient(160deg,#3d4d5c,#1f2a35)" role="img" aria-label="Engineer working at a computer"></div>
  <div class="photo" style="left:305px;top:437px;width:207px;height:138px;background:linear-gradient(135deg,#a98a78,#6b5a58)" role="img" aria-label="Hands typing on a laptop"></div>
  <h2 class="heading"><span class="mark"></span>Contact Us</h2>
  <div class="input" style="left:600px;top:215px;width:255px;height:52px">First Name:</div>
  <div class="input" style="left:877px;top:215px;width:255px;height:52px">Last Name:</div>
  <div class="input" style="left:600px;top:292px;width:255px;height:50px">Phone:</div>
  <div class="input" style="left:877px;top:292px;width:255px;height:50px">Email:</div>
  <div class="input" style="left:600px;top:366px;width:532px;height:129px">Mesage:</div>
  <a class="btn btn-blue">SUBMIT NOW <span class="arrow"><svg width="14" height="10" viewBox="0 0 14 10"><path d="M0 5h12M8 1l4 4-4 4" stroke="#fff" stroke-width="2" fill="none"/></svg></span></a>
</section>

<section class="clients">
  <div class="client" style="left:180px">Meridan</div>
  <div class="client" style="left:392px"><span class="sq"></span>Northvale</div>
  <div class="client" style="left:620px">Trovaline</div>
  <div class="client" style="left:846px"><span class="ci"></span>Solvera</div>
</section>

<footer class="site-footer">
  <div class="f-head" style="left:100px">Quick Links</div>
  <div class="f-head" style="left:351px">Our Services</div>
  <div class="f-head" style="left:869px">Contact Us</div>
  <div class="abs f-rule"></div>
  <ul class="f-list" style="left:98px"><li>Home</li><li>About Us</li><li>Services</li><li>Blog</li><li>Contact Us</li></ul>
  <ul class="f-list" style="left:348px"><li>Enterprise Systems Integration</li><li>Microservices</li><li>Platform Engineering</li><li>Conversation A.I.</li><li>iPaaS</li></ul>
  <ul class="f-list" style="left:624px;width:200px"><li>A.I. Agents</li><li>Real-time Data Stream<br>Processing</li><li>Flowtide</li><li>Technology Expertise</li></ul>
  <div class="f-contact" style="top:160px"><span class="ic"><svg width="14" height="14" viewBox="0 0 14 14"><path d="M3 1l3 3-2 2c1 2 2 3 4 4l2-2 3 3-2 2C6 13 1 8 1 3z" fill="var(--blue)"/></svg></span><span>CALL US<br>1800 555 014</span></div>
  <div class="f-contact" style="top:210px"><span class="ic"><svg width="14" height="12" viewBox="0 0 14 12"><rect x="1" y="1" width="12" height="10" fill="none" stroke="var(--blue)" stroke-width="1.6"/><path d="M1 1l6 5 6-5" fill="none" stroke="var(--blue)" stroke-width="1.6"/></svg></span><span>EMAIL US<br>hello@quarvendo.com</span></div>
  <div class="f-contact" style="top:262px"><span class="ic"><svg width="12" height="15" viewBox="0 0 12 15"><path d="M6 14C2 9 1 7 1 5a5 5 0 0 1 10 0c0 2-1 4-5 9z" fill="var(--blue)"/><circle cx="6" cy="5" r="2" fill="#fff"/></svg></span><span>Suite 210, 48 Harbour Lane<br>Melbourne, VIC , 3000</span></div>
  <div class="abs f-bottom"></div>
  <div class="abs copy">Copyright © 2025 All Rights Reserved By quarvendo</div>
  <span class="abs social" style="left:1048px"></span>
  <span class="abs social" style="left:1078px"></span>
  <span class="abs social" style="left:1108px"></span>
</footer>

</body>
</html>
```